Aid, Development & Consulting Firm

Brenvale Outhwaite Consulting Pty Ltd is a small firm in Australia whose principal works in the area of aid and development. His experience is broad ranging from aid project design and evaluation; to offering security advice in running aid operations in dangerous situations. He works with governments and private firms in conducting training for personnel travelling to work in dangerous or difficult regions. He has worked for many years with NGO's (aid organisations) and consults to the WCA. He works in locations all over the globe which include trouble spots like Iraq and Sudan, to sleepier locales like Samoa and Fiji. Being on Asia's doorstep much time is spent in Asia eg Indonesia, Vietnam. He is often called on to monitor and evaluate aid projects throughtout the globe.

Target Market(s)

Government Aid Divisions eg in Oz, KerenFund; WCA; NGO's and consulting firms who work in developing countries

Industry/Entity Type

Security

Requirements
Nice to have
• Try and incorporate a global feel without being obvious i.e. no starving children as the primary work done is a step beyond obvious aid relief. Something very simple but bold and stylish as card holder is not a "touchy" feely person
Should not have
• No starving kid type scenarios. Prefer no pictures

```html
<!DOCTYPE html>
<html lang="en">
<head>
<meta charset="utf-8">
<title>Brenvale Outhwaite Consulting – Business Card</title>
<link rel="stylesheet" href="https://fonts.googleapis.com/css2?family=Arimo:wght@400;700&family=Michroma&display=swap">
<style>
  :root {
    --stage-light: #ffffff;
    --stage-edge: #e2e3e5;
    --card-front: #000000;
    --card-back: #8a8b8f;
    --brand-blue: #1b9ad8;
    --icon-blue: #2a5d9c;
    --text-white: #ffffff;
    --faint-front: #3a3a3c;
    --faint-back: #7c7d81;
  }
  html, body {
    margin: 0;
    width: 1200px;
    height: 900px;
    overflow: hidden;
  }
  .stage {
    position: relative;
    width: 1200px;
    height: 900px;
    background: radial-gradient(ellipse at 50% 50%, var(--stage-light) 30%, var(--stage-edge) 100%);
    font-family: "Arimo", Arial, sans-serif;
  }
  .card {
    position: absolute;
    overflow: hidden;
    box-shadow: 0 1px 3px rgba(0,0,0,0.25);
  }
  .card-front {
    left: 263px; top: 30px; width: 673px; height: 411px;
    background: var(--card-front);
  }
  .card-back {
    left: 264px; top: 466px; width: 671px; height: 410px;
    background: var(--card-back);
  }
  .faint-disc {
    position: absolute;
    border-radius: 50%;
  }
  .card-front .faint-disc {
    left: 340px; top: 130px; width: 350px; height: 350px;
    background: radial-gradient(circle at 40% 40%, #4a4a4c 0%, var(--faint-front) 50%, #1a1a1a 100%);
    opacity: 0.8;
  }
  .card-back .faint-disc {
    left: 380px; top: 135px; width: 320px; height: 320px;
    background: var(--faint-back);
  }
  .brand-dot {
    position: absolute;
    left: 283px; top: 8px; width: 104px; height: 104px;
    border-radius: 50%;
    background: radial-gradient(circle at 55% 50%, #bfe6fb 0%, #45b3ea 40%, var(--brand-blue) 75%, #0f6fa8 100%);
  }
  .company-name {
    position: absolute;
    left: 0; right: 0; top: 133px;
    margin: 0;
    text-align: center;
    color: var(--text-white);
    font-weight: 700;
    font-size: 30px;
    letter-spacing: 0.2px;
  }
  .services {
    position: absolute;
    left: 0; right: 0; top: 176px;
    margin: 0;
    text-align: center;
    color: var(--brand-blue);
    font-family: "Michroma", "Arimo", sans-serif;
    font-size: 13px;
    letter-spacing: 2px;
    word-spacing: 2px;
  }
  .services .divider { margin: 0 14px; }
  .holder {
    position: absolute;
    left: 0; right: 0; top: 254px;
    text-align: center;
  }
  .holder-name {
    margin: 0;
    color: var(--text-white);
    font-weight: 700;
    font-size: 25px;
    letter-spacing: 1.2px;
    line-height: 28px;
  }
  .holder-role {
    margin: 0;
    color: var(--brand-blue);
    font-family: "Michroma", "Arimo", sans-serif;
    font-size: 18px;
    letter-spacing: 2px;
    font-variant: small-caps;
    line-height: 24px;
  }
  .contact {
    position: absolute;
    left: 52px; top: 134px;
    margin: 0; padding: 0;
    list-style: none;
    color: var(--text-white);
    font-size: 19.5px;
  }
  .contact li {
    position: relative;
    padding-left: 46px;
    line-height: 29px;
  }
  .contact .address { margin-bottom: 29px; }
  .contact svg {
    position: absolute;
    left: 4px;
    fill: var(--icon-blue);
  }
</style>
</head>
<body>
<main class="stage">
  <section class="card card-front" aria-label="Card front">
    <div class="faint-disc" aria-hidden="true"></div>
    <div class="brand-dot" aria-hidden="true"></div>
    <h1 class="company-name">Brenvale Outhwaite Consulting Pty Ltd</h1>
    <p class="services">AID<span class="divider">|</span>CONFLICT ANALYSIS<span class="divider">|</span>EVALUATION</p>
    <div class="holder">
      <p class="holder-name">B. Brenvale Outhwaite</p>
      <p class="holder-role">Director</p>
    </div>
  </section>

  <section class="card card-back" aria-label="Card back">
    <div class="faint-disc" aria-hidden="true"></div>
    <ul class="contact">
      <li class="address">
        <svg width="18" height="32" viewBox="0 0 18 32" style="top:3px" aria-hidden="true"><path d="M9 0C4 0 0 4 0 9c0 6 9 23 9 23s9-17 9-23C18 4 14 0 9 0z"/></svg>
        42 Harlow Street<br>Kelmscott Park<br>SA 5099 Australia
      </li>
      <li>
        <svg width="26" height="22" viewBox="0 0 26 22" style="top:3px" aria-hidden="true"><path d="M1 7c0-4 5-6 12-6s12 2 12 6v2h-6V6H7v3H1z"/><path d="M5 10h16l3 11H2z"/><circle cx="13" cy="15" r="3" fill="#8a8b8f"/></svg>
        +61 8 7010 4821
      </li>
      <li>
        <svg width="18" height="28" viewBox="0 0 18 28" style="top:1px" aria-hidden="true"><path d="M3 0h12a3 3 0 0 1 3 3v22a3 3 0 0 1-3 3H3a3 3 0 0 1-3-3V3a3 3 0 0 1 3-3zm0 4v18h12V4z"/><circle cx="9" cy="25" r="1.5" fill="#8a8b8f"/></svg>
        +61 (0) 491 570 156
      </li>
      <li>
        <svg width="26" height="18" viewBox="0 0 26 18" style="top:7px" aria-hidden="true"><path d="M0 0h26v18H0zm2 2v14h22V2z"/><path d="M2 2l11 9 11-9v2L13 13 2 4z"/><path d="M2 16l8-7 1 1-8 7zM24 16l-8-7-1 1 8 7z"/></svg>
        brenvale@mailhollow.com
      </li>
      <li>
        <svg width="26" height="18" viewBox="0 0 26 18" style="top:7px" aria-hidden="true"><path d="M0 0h26v18H0zm2 2v14h22V2z"/><path d="M2 2l11 9 11-9v2L13 13 2 4z"/><path d="M2 16l8-7 1 1-8 7zM24 16l-8-7-1 1 8 7z"/></svg>
        brenvaleo@postwell.com
      </li>
    </ul>
  </section>
</main>
</body>
</html>
```